Whisking Wonderful cooking school - folded brochure

BROCHURE DESIGN BRIEF
Project Overview

I own a cooking school and recently published my cookbook. I’m looking for a talented graphic designer to create a modern, visually stunning accordion-fold brochure that reflects the quality of my brand and motivates people to take action.

Primary Goals

The brochure should:

Sell my cookbook, Whisking Wonderful
Generate registrations for cooking classes
Drive visitors to my website
Encourage calls and emails for more information

Every design decision should support these goals.

Target Audience
Adults interested in cooking and entertaining
Parents of middle and high school students
Families preparing teens for college
Businesses seeking corporate team-building experiences
Programs to Feature

Adult Cooking

Private lessons
Couples
Small groups
Friends’ nights out
Special events

Teen Cooking

Grades 7–9
Campus Ready Course — Grades 10–12

IMPORTANT: Prominently feature that we are a Bright Path Learners Approved Provider, using both the Bright Path Learners logo and my company logo.

Corporate Team Building
Interactive culinary experiences for businesses, including employee appreciation, leadership development, and team-building events.

Cookbook

Include a dedicated section promoting my recently published cookbook:

Whisking Wonderful

More than a recipe book, it teaches cooking skills, techniques, meal prep, hosting tips, and kitchen confidence.

The brochure should create excitement and encourage readers to purchase the cookbook.

Design Direction

The attached brochure is NOT the direction I want. It feels dated, cluttered, and lacks visual impact.

I’m looking for a design that is:

Modern
Clean and upscale
Warm and inviting
Editorial / magazine-inspired
Easy to read
Food-focused with beautiful imagery
Visually sophisticated
Strong calls to action

Think Hartley Provence, Chez Le Four, Basket & Jar, or a premium food magazine—not a traditional flyer.

Format
Final size: 14" × 8.5"
Accordion / Z-fold
Professionally printed
Include proper bleed, safe margins, and accurate fold placement
Resources I Will Provide
Company logo
Bright Path Learners logo
Cookbook cover
Photos
Website
Brand colors, if needed

My website contains detailed information about all programs and may be used as inspiration for organizing the content.

Overall Objective

When someone picks up this brochure, I want them to immediately think:

“This looks professional, exciting, and different. I want to buy the cookbook and sign up for a class.”

The brochure should feel less like an advertisement and more like a beautifully designed culinary lifestyle piece—something that inspires people to cook, learn, and connect through food.

Target Market(s)

Adults and Teenagers who have a passion for learning

Industry/Entity Type

cooking school

Font styles to use
Other font styles liked:
• more sugar font (maybe)

Requirements
Must have
• many call to actions to sign up for classes and to buy cookbook
Nice to have
• modern, clean feel, classes are higher end (expensive) I like colors on my Website so everything will look like it compliments each other (doesn't have to match exactly) but should feel the style of my website
Should not have
• no clutter.

```html
<!DOCTYPE html>
<html lang="en">
<head>
<meta charset="utf-8">
<title>Whisking Wonderful – Brochure Spreads</title>
<link rel="stylesheet" href="https://fonts.googleapis.com/css2?family=Bebas+Neue&family=Poppins:wght@400;500;600;700&family=Libre+Baskerville:ital@0;1&family=Kaushan+Script&display=swap">
<style>
  :root{
    --backdrop:#211f1e;
    --cocoa:#5f5046;
    --cocoa-deep:#4c4038;
    --cream:#f7efe6;
    --cream-light:#fbf6ef;
    --peach:#f2e0d0;
    --slate:#5b7186;
    --clay:#9a6b58;
    --sand:#d6b89c;
    --ink:#4a3e36;
    --rule:#a0725c;
    --white:#ffffff;
  }
  *{box-sizing:border-box;margin:0;padding:0}
  html,body{width:947px;height:1200px;overflow:hidden;background:var(--backdrop)}
  body{position:relative;font-family:'Poppins',sans-serif;color:var(--ink)}
  .spread{position:absolute;left:60px;width:832px;overflow:hidden}
  .spread--outside{top:65px;height:511px}
  .spread--inside{top:624px;height:509px;width:830px}
  .panel{position:absolute;top:0;height:100%}
  .abs{position:absolute}
  .photo{position:absolute}
  .heading{font-family:'Bebas Neue',sans-serif;color:var(--ink);letter-spacing:.3px;font-weight:400}
  .serif-italic{font-family:'Libre Baskerville',serif;font-style:italic}
  .brand{font-family:'Poppins',sans-serif;font-weight:600;color:var(--cocoa);line-height:1}

  /* Outside spread */
  .about{left:0;width:279px;background:linear-gradient(180deg,var(--cream-light),#fbf3e6)}
  .about__meet{left:33px;top:20px;font-size:18px;color:var(--clay)}
  .about__name{left:32px;top:40px;font-size:23px}
  .about__portrait{left:17px;top:98px;width:140px;height:274px;background:linear-gradient(180deg,#f3ede6 0%,#e9e2da 40%,#d9c3a8 75%,#f0ece7 100%);border-radius:60px 60px 4px 4px}
  .about__story{left:164px;top:77px;width:104px;font-size:6.4px;line-height:7.75px;color:#3b332d}
  .about__story p{margin-bottom:7.5px}
  .about__band{left:0;top:0;width:279px;height:511px}
  .about__closing{left:22px;top:394px;width:164px;font-size:6.7px;line-height:7.8px;color:#f3e9df}
  .about__closing p{margin-bottom:7px}
  .about__sign{font-size:8px;font-weight:500;line-height:9px;color:var(--white)}
  .about__sign small{font-size:7px;display:block}
  .about__snapshot{left:188px;top:396px;width:79px;height:97px;background:var(--cream);padding:3px;transform:rotate(3deg)}
  .about__snapshot div{width:100%;height:100%;background:linear-gradient(160deg,#6b5a4c,#d8cfc6 55%,#a87a45)}

  .recipes{left:279px;width:273px;background:linear-gradient(90deg,#efdccc,var(--peach) 12%,#f6e7da)}
  .recipes__title{left:0;width:273px;top:31px;text-align:center;font-size:23px}
  .recipe{left:29px;width:218px}
  .recipe__img{width:218px;height:90px}
  .recipe__label{margin-top:2px;height:19px;background:var(--slate);color:var(--white);font-family:'Bebas Neue',sans-serif;font-size:10.5px;letter-spacing:.3px;display:flex;align-items:center;justify-content:center;text-align:center}
  .course{left:26px;width:224px;top:431px;text-align:center}
  .course__title{border-top:.6px solid var(--ink);border-bottom:.6px solid var(--ink);font-family:'Bebas Neue',sans-serif;font-size:12.5px;padding:2px 0 1px;color:var(--ink)}
  .course__note{font-size:5.4px;line-height:6.6px;margin-top:3px;color:#3b332d}

  .cover{left:552px;width:280px;background:linear-gradient(180deg,#f6e8dc,#efdccb 45%,#e5cbb4)}
  .cover__brand{left:0;width:280px;top:40px;text-align:center;font-size:28px}
  .cover__brand span{display:block;font-size:18px;margin-top:4px;padding-left:70px}
  .cover__tagline{left:0;width:280px;top:142px;text-align:center;font-family:'Libre Baskerville',serif;font-size:15.5px;line-height:20px;color:var(--clay)}
  .cover__script{left:0;width:280px;top:176px;text-align:center;font-family:'Kaushan Script',cursive;font-size:40px;color:var(--ink)}
  .cover__swash{left:110px;top:226px}
  .cover__photo{left:0;top:250px;width:280px;height:261px;background:radial-gradient(ellipse at 55% 60%,#e4a95a 0%,#b9763d 35%,#6e4a30 70%,#4a382c 100%);-webkit-mask-image:linear-gradient(180deg,transparent 0,#000 18%);mask-image:linear-gradient(180deg,transparent 0,#000 18%)}

  .cta-bar{left:279px;top:472px;width:553px;height:22px;background:var(--cocoa-deep);display:flex;align-items:center}
  .cta-bar__text{width:273px;padding-left:28px;font-weight:700;font-size:10.2px;color:var(--white);letter-spacing:.2px}
  .cta-bar__web{width:280px;text-align:center;font-family:'Libre Baskerville',serif;font-size:12.5px;color:var(--white)}

  /* Inside spread */
  .classes{left:0;width:279px;background:var(--cream)}
  .section-title{text-align:center;font-size:21px;line-height:25px}
  .section-rule{position:absolute;height:1.2px;width:44px;background:var(--rule)}
  .section-lead{text-align:center;font-size:9.3px;line-height:11px;color:#3b332d}
  .band{left:0;top:0}
  .class-card{left:35px;width:213px;height:124px;border:2px solid #e9ddd0}
  .class-card__img{position:absolute;inset:0}
  .class-card__box{position:absolute;left:0;bottom:0;width:86px;background:rgba(91,113,134,.92);padding:8px 6px 6px 9px;color:var(--white)}
  .class-card__title{font-family:'Bebas Neue',sans-serif;font-size:12.5px;margin-bottom:4px}
  .class-card__list{list-style:none;font-size:6.5px;line-height:9.8px}
  .class-card__list li{display:flex;gap:3px;align-items:flex-start}
  .class-card__list svg{flex:none;margin-top:2px}
  .classes__motto{left:0;width:279px;top:424px;text-align:center;font-size:10.8px;line-height:13px;color:#efe3d6}
  .classes__brand{left:0;width:279px;top:462px;text-align:center;font-size:17px;color:#f3e9df}

  .cookbook{left:279px;width:272px;background:linear-gradient(90deg,#efe3d7,#f6ede3 15%,var(--cream))}
  .cookbook__brand{left:0;width:272px;top:26px;text-align:center;font-size:27px}
  .cookbook__brand span{display:block;font-size:17px;margin-top:3px;padding-left:60px}
  .cookbook__list{list-style:none;left:62px;top:185px;font-size:9.2px;line-height:13.8px;color:#3b332d}
  .cookbook__list li{display:flex;align-items:center;gap:4px}
  .cookbook__photo{left:0;top:277px;width:272px;height:232px;background:radial-gradient(ellipse at 50% 55%,#b8bcb5 0%,#a18468 38%,#6d5040 70%,#4a372b 100%)}

  .corporate{left:551px;width:279px;background:linear-gradient(90deg,#efe4d8,var(--cream) 12%)}
  .benefit{left:58px;display:flex;align-items:center;gap:10px}
  .benefit__icon{width:47px;height:47px;border-radius:50%;display:flex;align-items:center;justify-content:center}
  .benefit__label{font-weight:600;font-size:9px;line-height:11px;color:var(--clay);letter-spacing:.2px}
  .dash{left:115px;width:133px;border-top:.8px dashed #b99b88}
  .provider{left:46px;top:322px;width:199px;height:121px;border:.8px solid #d9cbbf}
  .provider__head{height:34px;background:var(--cocoa-deep);color:var(--white);font-weight:600;font-size:10px;line-height:12.5px;text-align:center;padding-top:4px}
  .provider__mark{display:flex;align-items:center;justify-content:center;gap:7px;height:86px;color:var(--white);font-weight:500;font-size:13px}
  .provider__mark i{display:block;width:16px;height:16px;border-radius:50%;background:var(--white)}
  .corporate__motto{left:0;width:279px;top:451px;text-align:center;font-size:8.4px;color:#efe3d6}
  .corporate__mail{left:132px;top:466px}
  .corporate__web{left:0;width:279px;top:481px;text-align:center;font-size:9px;color:var(--white)}
</style>
</head>
<body>

<!-- Outside spread -->
<section class="spread spread--outside">

  <div class="panel about">
    <p class="abs about__meet serif-italic">Meet</p>
    <h2 class="abs about__name heading">Chef Marla Castellane</h2>
    <div class="abs about__portrait" role="img" aria-label="Chef in white jacket and toque holding a baked pie on a glass cake stand"></div>
    <div class="abs about__story">
      <p>For me, food has always been about bringing people together. I raised my three kids around the kitchen table—talking about our days, laughing, sometimes disagreeing, but always finding our way back to one another. Cooking was never just about the meal; it was about connection.</p>
      <p>I’ve had many chapters in my life, but this—this is my passion. The kind you feel in your bones. And if you’ve ever been invited into my home, you know… it’s where I come alive. I love an intimate dinner party. I enjoy cooking, but baking is my happy place. And while I appreciate a beautiful restaurant, nothing compares to the feeling of gathering people I love around my own table.</p>
      <p>After more than 40 years in the kitchen, what stays with me most isn’t just the food—it’s the memories. In a world that moves too fast and lives on screens, I believe deeply in carving out time to sit, talk, and truly be present.</p>
    </div>
    <svg class="abs about__band" width="279" height="511" viewBox="0 0 279 511" aria-hidden="true">
      <polygon points="0,348 28,375 251,375 279,348 279,511 0,511" fill="var(--cocoa)"/>
    </svg>
    <div class="abs about__closing">
      <p>My philosophy is simple: cook at home, cook with heart, and cook for the people you love.</p>
      <p>I want to share that feeling—that warmth, that joy, that sense of connection. Because great food doesn’t have to be complicated, and your kitchen can be the happiest room in your home.</p>
      <p>Here’s to cooking boldly, joyfully, and a little bit rebelliously.</p>
      <p class="about__sign">Marla Castellane<small>Founder, Chef &amp; Author</small></p>
    </div>
    <div class="abs about__snapshot"><div role="img" aria-label="Chef smiling while serving a baked casserole in a home kitchen"></div></div>
  </div>

  <div class="panel recipes">
    <h2 class="abs recipes__title heading">Recipes You Love</h2>
    <figure class="abs recipe" style="top:65px">
      <div class="recipe__img" role="img" aria-label="Bowl of golden lentil and squash soup topped with pumpkin seeds and cilantro" style="background:radial-gradient(ellipse at 50% 45%,#e9b22c 0%,#d99a1f 45%,#4b4a48 80%,#2e2d2c 100%)"></div>
      <figcaption class="recipe__label">African Lentil &amp; Butternut Squash Soup</figcaption>
    </figure>
    <figure class="abs recipe" style="top:187px">
      <div class="recipe__img" role="img" aria-label="Bowl of chicken stir-fry with red peppers, zucchini and peanuts" style="background:radial-gradient(ellipse at 50% 45%,#c9803a 0%,#a9452b 35%,#6e6a62 70%,#b49d80 100%)"></div>
      <figcaption class="recipe__label">Kung Pao Chicken Stir-Fry with Peppers and Peanuts</figcaption>
    </figure>
    <figure class="abs recipe" style="top:308px">
      <div class="recipe__img" role="img" aria-label="Lemon bar dusted with powdered sugar beside fresh mint on slate" style="background:linear-gradient(100deg,#3b4045 0%,#e9e2cf 35%,#f2ecda 50%,#3e5a2e 75%,#2e3b24 100%)"></div>
      <figcaption class="recipe__label">Lemon Bars with Creamy Custard Filling</figcaption>
    </figure>
    <div class="abs course">
      <p class="course__title">Join us 4-week cooking course (meet 1x per week)</p>
      <p class="course__note">designed specifically for high school students grades 10–12th.<br>Small classes. Real skills, Delicious results.</p>
    </div>
  </div>

  <div class="panel cover">
    <p class="abs brand cover__brand">Whisking<span>Wonderful</span></p>
    <p class="abs cover__tagline">Cooking made Fun,<br>Fast, and Whisking</p>
    <p class="abs cover__script">Wonderful</p>
    <svg class="abs cover__swash" width="80" height="14" viewBox="0 0 80 14" aria-hidden="true">
      <path d="M2 10 Q40 -2 78 8" fill="none" stroke="var(--ink)" stroke-width="1.6" stroke-linecap="round"/>
    </svg>
    <div class="abs cover__photo" role="img" aria-label="Slices of salmon quiche with asparagus, eggs and tomatoes on a rustic table"></div>
  </div>

  <div class="abs cta-bar">
    <p class="cta-bar__text">SIGN UP TODAY OR TEXT 555-014-2290</p>
    <p class="cta-bar__web">www.whiskingwonderful.com</p>
  </div>
</section>

<!-- Inside spread -->
<section class="spread spread--inside">

  <div class="panel classes">
    <h2 class="abs heading section-title" style="left:0;width:279px;top:31px">Cooking Classes for<br>Every Stages</h2>
    <span class="section-rule" style="left:118px;top:85px"></span>
    <p class="abs section-lead" style="left:0;width:279px;top:98px">Hands-on classes that build real skills<br>and lifelong confidence.</p>
    <svg class="abs band" width="279" height="509" viewBox="0 0 279 509" aria-hidden="true">
      <polygon points="0,277 28,303 251,303 279,277 279,509 0,509" fill="var(--cocoa)"/>
    </svg>
    <div class="abs class-card" style="top:152px">
      <div class="class-card__img" role="img" aria-label="Two women laughing while cooking together in red aprons" style="background:linear-gradient(100deg,#8a6a4c 0%,#c8503e 35%,#b23a32 55%,#4e4634 80%,#cfc6bb 100%)"></div>
      <div class="class-card__box">
        <p class="class-card__title">ADULT COOKING</p>
        <ul class="class-card__list">
          <li><svg width="5" height="5" viewBox="0 0 5 5"><path d="M2 0h1v2h2v1H3v2H2V3H0V2h2z" fill="#fff"/></svg>Private lessons</li>
          <li><svg width="5" height="5" viewBox="0 0 5 5"><path d="M2 0h1v2h2v1H3v2H2V3H0V2h2z" fill="#fff"/></svg>Couples</li>
          <li><svg width="5" height="5" viewBox="0 0 5 5"><path d="M2 0h1v2h2v1H3v2H2V3H0V2h2z" fill="#fff"/></svg>Small groups</li>
          <li><svg width="5" height="5" viewBox="0 0 5 5"><path d="M2 0h1v2h2v1H3v2H2V3H0V2h2z" fill="#fff"/></svg>Friends’ nights out</li>
          <li><svg width="5" height="5" viewBox="0 0 5 5"><path d="M2 0h1v2h2v1H3v2H2V3H0V2h2z" fill="#fff"/></svg>Special events</li>
        </ul>
      </div>
    </div>
    <div class="abs class-card" style="top:290px">
      <div class="class-card__img" role="img" aria-label="Teen student in chef hat chopping vegetables with the chef" style="background:linear-gradient(100deg,#3c3c3a 0%,#8d8a84 30%,#eeeeec 55%,#d8d4cf 75%,#b5473a 100%)"></div>
      <div class="class-card__box">
        <p class="class-card__title">TEEN COOKING</p>
        <ul class="class-card__list">
          <li><svg width="5" height="5" viewBox="0 0 5 5"><path d="M2 0h1v2h2v1H3v2H2V3H0V2h2z" fill="#fff"/></svg>Grades 7–9</li>
          <li><svg width="5" height="5" viewBox="0 0 5 5"><path d="M2 0h1v2h2v1H3v2H2V3H0V2h2z" fill="#fff"/></svg>Campus Ready Course — Grades 10–12</li>
        </ul>
      </div>
    </div>
    <p class="abs classes__motto serif-italic">Build skills. Make memories.<br>Prepare for what’s next.</p>
    <p class="abs brand classes__brand">Whisking Wonderful</p>
  </div>

  <div class="panel cookbook">
    <p class="abs brand cookbook__brand">Whisking<span>Wonderful</span></p>
    <h2 class="abs heading section-title" style="left:0;width:272px;top:105px">Our Cookbook</h2>
    <span class="section-rule" style="left:114px;top:131px"></span>
    <p class="abs section-lead" style="left:18px;width:236px;top:142px">More than a recipe book, it teaches cooking skills, techniques, meal prep, hosting tips, and kitchen confidence.</p>
    <ul class="abs cookbook__list">
      <li><svg width="7" height="7" viewBox="0 0 5 5"><path d="M2 0h1v2h2v1H3v2H2V3H0V2h2z" fill="var(--ink)"/></svg>Recipes for Every Occasion</li>
      <li><svg width="7" height="7" viewBox="0 0 5 5"><path d="M2 0h1v2h2v1H3v2H2V3H0V2h2z" fill="var(--ink)"/></svg>Essential Cooking Techniques</li>
      <li><svg width="7" height="7" viewBox="0 0 5 5"><path d="M2 0h1v2h2v1H3v2H2V3H0V2h2z" fill="var(--ink)"/></svg>Meal Prep Made Simple</li>
      <li><svg width="7" height="7" viewBox="0 0 5 5"><path d="M2 0h1v2h2v1H3v2H2V3H0V2h2z" fill="var(--ink)"/></svg>Hosting Tips &amp; Entertaining Ideas</li>
      <li><svg width="7" height="7" viewBox="0 0 5 5"><path d="M2 0h1v2h2v1H3v2H2V3H0V2h2z" fill="var(--ink)"/></svg>Build Confidence, Create More</li>
    </ul>
    <div class="abs cookbook__photo" role="img" aria-label="Cookbook cover with an apron illustration lying on a wooden board with spoons, herbs and linen"></div>
  </div>

  <div class="panel corporate">
    <h2 class="abs heading section-title" style="left:0;width:279px;top:29px">Corporate Team Building</h2>
    <span class="section-rule" style="left:118px;top:61px"></span>
    <p class="abs section-lead" style="left:8px;width:263px;top:67px">Interactive culinary experiences for businesses bring teams together-boosting morale, encouraging collaboration, and creating lasting connections.</p>

    <div class="abs benefit" style="top:114px">
      <span class="benefit__icon" style="background:var(--clay)">
        <svg width="28" height="24" viewBox="0 0 28 24" fill="none" stroke="#fff" stroke-width="1.2"><circle cx="14" cy="7" r="3.5"/><circle cx="6" cy="9" r="2.6"/><circle cx="22" cy="9" r="2.6"/><path d="M8 22v-5a6 6 0 0 1 12 0v5M1.5 20v-3a4.5 4.5 0 0 1 6-4M26.5 20v-3a4.5 4.5 0 0 0-6-4"/></svg>
      </span>
      <p class="benefit__label">EMPLOYEE<br>APPRECIATION</p>
    </div>
    <span class="abs dash" style="top:167px"></span>
    <div class="abs benefit" style="top:173px">
      <span class="benefit__icon" style="background:var(--sand)">
        <svg width="24" height="23" viewBox="0 0 24 23"><path d="M12 1l3.3 7 7.6.9-5.6 5.2 1.5 7.5L12 17.8 5.2 21.6l1.5-7.5L1.1 8.9l7.6-.9z" fill="#fff"/></svg>
      </span>
      <p class="benefit__label">LEADERSHIP<br>DEVELOPMENT</p>
    </div>
    <span class="abs dash" style="top:226px"></span>
    <div class="abs benefit" style="top:230px">
      <span class="benefit__icon" style="background:var(--clay)">
        <svg width="26" height="22" viewBox="0 0 26 22"><path d="M13 21S1 13.5 1 6.6A5.8 5.8 0 0 1 13 4a5.8 5.8 0 0 1 12 2.6C25 13.5 13 21 13 21z" fill="#fff"/></svg>
      </span>
      <p class="benefit__label">TEAM-BUILDING<br>EVENTS</p>
    </div>

    <svg class="abs band" width="279" height="509" viewBox="0 0 279 509" aria-hidden="true">
      <polygon points="0,275 34,303 246,303 279,277 279,509 0,509" fill="var(--cocoa)"/>
    </svg>
    <div class="abs provider">
      <p class="provider__head">BRIGHT PATH LEARNERS<br>APPROVED PROVIDER</p>
      <p class="provider__mark"><i></i>Bright Path Learners</p>
    </div>
    <p class="abs corporate__motto serif-italic">investing in today’s learners for a strong tomorrow.</p>
    <svg class="abs corporate__mail" width="14" height="10" viewBox="0 0 14 10" fill="none" stroke="#fff" stroke-width="1.1" aria-label="Email"><rect x=".6" y=".6" width="12.8" height="8.8" rx="1"/><path d="M.8 1l6.2 4.6L13.2 1"/></svg>
    <p class="abs corporate__web">www.whiskingwonderful.com</p>
  </div>
</section>

</body>
</html>
```